Larkspur Ridge Management - Business Cards

I need business cards. My current logo was designed by a designer at this site and I very much like and am happy with the results. I would like a business card that is trendy, unique, current yet professional. I deal with high net worth clients daily

Target Market(s)

Out of state investors looking to get into the rental market in Ohio

Industry/Entity Type

Property Management, Consulting

Contact Information for Business Card

Name, Title (Chief Financial Officer) office phone number (555) 817-3094 website address larkridgemgmt.example

Font styles to use
Sans Serif

Colors
0054AA
0677BA
7BADD7
CADEEF
E8F1F8
0094D4
00A9DD
6FCCEA
C7EBF8
E9F6FB
00AB8E
00BBA5
67D7C9
C6EFE9
E9F9F6

```html
<!DOCTYPE html>
<html lang="en">
<head>
<meta charset="utf-8">
<title>Larkspur Ridge Management – Business Cards</title>
<link rel="stylesheet" href="https://fonts.googleapis.com/css2?family=Montserrat:wght@400;600;800&display=swap">
<style>
  :root {
    --navy: #24375e;
    --navy-deep: #1f2f52;
    --red: #d3303a;
    --white: #ffffff;
    --stage: #e9ecf0;
    --muted-line: rgba(255,255,255,0.35);
  }
  * { box-sizing: border-box; margin: 0; padding: 0; }
  html, body {
    width: 1200px; height: 1200px; overflow: hidden;
    background: var(--stage);
    font-family: "Montserrat", sans-serif;
  }
  .sheet {
    width: 1200px; height: 1200px;
    display: flex; flex-direction: column; align-items: center; justify-content: center;
    gap: 64px;
  }
  .card {
    position: relative;
    width: 840px; height: 480px;
    border-radius: 34px;
    overflow: hidden;
    box-shadow: 0 10px 30px rgba(20,30,50,0.18);
  }

  /* Front */
  .card--front { background: var(--white); }
  .front__brand {
    position: absolute; left: 0; right: 0; top: 0; height: 250px;
    display: flex; align-items: center; justify-content: center; gap: 18px;
  }
  .brand-mark {
    width: 26px; height: 26px; border-radius: 50%;
    background: var(--red);
  }
  .brand-name {
    font-weight: 800; font-size: 34px; letter-spacing: 1px;
    text-transform: uppercase; line-height: 1.1; text-align: left;
  }
  .front__brand .brand-name { color: var(--navy); }
  .front__stripe {
    position: absolute; left: 0; right: 0; top: 250px; height: 9px;
    background: var(--red);
  }
  .front__band {
    position: absolute; left: 0; right: 0; top: 268px; bottom: 0;
    background: var(--navy);
    display: grid; grid-template-columns: 1fr 1px 1fr; align-items: center;
    padding: 0 56px;
  }
  .person { padding-right: 30px; }
  .person__name {
    color: var(--red); font-weight: 600; font-size: 36px; letter-spacing: 1.5px;
    text-transform: uppercase; line-height: 1.1;
  }
  .person__title {
    color: var(--white); font-weight: 400; font-size: 17px; letter-spacing: 1px;
    text-transform: uppercase; margin-top: 6px;
  }
  .band__divider { width: 1px; height: 120px; background: var(--muted-line); }
  .contact { list-style: none; padding-left: 44px; }
  .contact__item {
    display: flex; align-items: center; gap: 14px;
    color: var(--white); font-size: 22px; font-weight: 400; letter-spacing: 0.5px;
  }
  .contact__item + .contact__item { margin-top: 16px; }
  .contact__icon { width: 26px; height: 26px; flex: none; }

  /* Back */
  .card--back {
    background: radial-gradient(ellipse at 50% 35%, #2b4069 0%, var(--navy) 55%, var(--navy-deep) 100%);
    display: flex; align-items: center; justify-content: center; gap: 24px;
  }
  .card--back .brand-mark { width: 36px; height: 36px; }
  .card--back .brand-name { color: var(--white); font-size: 46px; }
</style>
</head>
<body>
<main class="sheet">

  <section class="card card--front" aria-label="Business card front">
    <div class="front__brand">
      <span class="brand-mark" aria-hidden="true"></span>
      <p class="brand-name">Larkspur Ridge<br>Management</p>
    </div>
    <div class="front__stripe" aria-hidden="true"></div>
    <div class="front__band">
      <div class="person">
        <p class="person__name">Full Name</p>
        <p class="person__title">Chief Financial Officer</p>
      </div>
      <span class="band__divider" aria-hidden="true"></span>
      <ul class="contact">
        <li class="contact__item">
          <svg class="contact__icon" viewBox="0 0 24 24" aria-hidden="true">
            <path fill="#d3303a" d="M6.6 10.8a15.1 15.1 0 0 0 6.6 6.6l2.2-2.2a1 1 0 0 1 1-.25 11.4 11.4 0 0 0 3.6.57 1 1 0 0 1 1 1V20a1 1 0 0 1-1 1A17 17 0 0 1 3 4a1 1 0 0 1 1-1h3.5a1 1 0 0 1 1 1c0 1.25.2 2.45.57 3.57a1 1 0 0 1-.25 1z"/>
          </svg>
          <span>(555) 817-3094</span>
        </li>
        <li class="contact__item">
          <svg class="contact__icon" viewBox="0 0 24 24" aria-hidden="true" fill="none" stroke="#d3303a" stroke-width="1.8">
            <circle cx="12" cy="12" r="9.5"/>
            <ellipse cx="12" cy="12" rx="4.2" ry="9.5"/>
            <line x1="2.5" y1="12" x2="21.5" y2="12"/>
            <line x1="4" y1="7" x2="20" y2="7"/>
            <line x1="4" y1="17" x2="20" y2="17"/>
          </svg>
          <span>larkridgemgmt.example</span>
        </li>
      </ul>
    </div>
  </section>

  <section class="card card--back" aria-label="Business card back">
    <span class="brand-mark" aria-hidden="true"></span>
    <p class="brand-name">Larkspur Ridge<br>Management</p>
  </section>

</main>
</body>
</html>
```